Tavrel Fitness business cards

I need a business card for my company called Tavrel Fitness. I am a certified personal trainer, QMB certified, Hippo Pilates certified, and Vital paths certified. I am also an independent KORVEL rep, the number #1 rated nutritional and supplement product in the country. The card needs to convey Health, Wellness, Living Life and Loving It. I want it to be clean, sharp, eye-catching. Tantalizing.
Updates

for some reason, I'm unable to upload the pics I need. Stay tuned..

Industry/Entity Type

Business

Contact Information for Business Card

Tavrel Fitness
Mona Lykkestad, Owner
mona@tavrelfitness-example.com
555-203-4471
tavrelfitness-example.com
mona@tavrelfitness-example.com

Font styles to use
Serif

Requirements
Must have
• Must use pic of me and KORVEL logo

```html
<!DOCTYPE html>
<html lang="en">
<head>
<meta charset="utf-8">
<title>Tavrel Fitness – Business Cards</title>
<link rel="stylesheet" href="https://fonts.googleapis.com/css2?family=Cinzel:wght@500;600&family=Lora:wght@400;500&display=swap">
<style>
  :root {
    --stage: #2b2b2b;
    --card-light: #ffffff;
    --card-mid: #e4e4e4;
    --card-dark: #c9c9c9;
    --brand-blue: #00aeef;
    --ink: #3a3a3a;
    --white: #ffffff;
    --photo-tone: #b9c4cc;
  }
  * { box-sizing: border-box; margin: 0; padding: 0; }
  html, body { width: 1200px; height: 870px; overflow: hidden; }
  body {
    background: var(--stage);
    position: relative;
    font-family: "Lora", serif;
  }
  .card {
    position: absolute;
    width: 640px;
    height: 366px;
    overflow: hidden;
    box-shadow: 0 10px 30px rgba(0,0,0,.45);
  }
  .card--back {
    left: 120px; top: 46px;
    background: radial-gradient(ellipse at 55% 45%, var(--card-light) 0%, var(--card-mid) 65%, var(--card-dark) 100%);
  }
  .card--front {
    left: 440px; top: 458px;
    background: var(--brand-blue);
  }
  .wordmark {
    font-family: "Cinzel", serif;
    font-weight: 600;
    color: var(--brand-blue);
    letter-spacing: 3px;
    line-height: 1;
    white-space: nowrap;
  }
  .back__photo {
    position: absolute; left: 44px; top: 98px;
    width: 130px; height: 170px;
    background: linear-gradient(160deg, #d3dbe0 0%, var(--photo-tone) 100%);
  }
  .back__wordmark {
    position: absolute; left: 200px; top: 158px;
    font-size: 40px;
  }
  .partner {
    position: absolute; right: 30px; bottom: 24px;
    display: flex; align-items: center; gap: 8px;
    font-family: "Lora", serif; font-weight: 500;
    font-size: 15px; letter-spacing: 2px; color: var(--ink);
  }
  .partner__dot {
    width: 14px; height: 14px; border-radius: 50%;
    background: var(--ink);
  }
  .front__top {
    position: absolute; left: 0; top: 0; right: 0; height: 200px;
    background: radial-gradient(ellipse at 60% 40%, var(--card-light) 0%, var(--card-mid) 70%, var(--card-dark) 100%);
  }
  .contact-list {
    position: absolute; left: 30px; top: 24px;
    list-style: none;
    font-size: 13px; color: var(--ink);
  }
  .contact-list li {
    display: flex; align-items: center; gap: 10px;
    height: 28px;
  }
  .contact-list svg { width: 16px; height: 16px; fill: var(--ink); flex: none; }
  .front__brand {
    position: absolute; right: 34px; top: 52px;
  }
  .front__brand .wordmark { display: block; font-size: 42px; }
  .front__brand .wordmark + .wordmark { margin-top: 16px; }
  .address {
    position: absolute; left: 30px; top: 236px;
    color: var(--white); font-size: 17px; line-height: 1.4;
    font-family: "Lora", serif; font-weight: 500;
    letter-spacing: .5px;
  }
  .holder {
    position: absolute; right: 34px; bottom: 34px;
    text-align: right; color: var(--white);
  }
  .holder__name {
    font-family: "Cinzel", serif; font-weight: 600;
    font-size: 20px; letter-spacing: 1px;
  }
  .holder__role { font-size: 15px; margin-top: 4px; letter-spacing: .5px; }
</style>
</head>
<body>

<section class="card card--back" aria-label="Card back">
  <div class="back__photo" role="img" aria-label="Portrait photo of Mona Lykkestad"></div>
  <span class="wordmark back__wordmark">Tavrel Fitness</span>
  <div class="partner"><span class="partner__dot"></span>KORVEL</div>
</section>

<section class="card card--front" aria-label="Card front">
  <div class="front__top">
    <ul class="contact-list">
      <li>
        <svg viewBox="0 0 16 16" aria-hidden="true"><path d="M4 1l3 3-1.6 1.8c.8 1.8 2.2 3.2 4 4L11.2 8.5 14.5 11.5 12.6 14C7 13.5 2.5 9 2 3.4z"/></svg>
        555-203-4471
      </li>
      <li>
        <svg viewBox="0 0 16 16" aria-hidden="true"><path d="M5 1h6a1 1 0 0 1 1 1v12a1 1 0 0 1-1 1H5a1 1 0 0 1-1-1V2a1 1 0 0 1 1-1zm.5 2v9h5V3zM8 12.6a.8.8 0 1 0 0 1.6.8.8 0 0 0 0-1.6z"/></svg>
        555-203-4471
      </li>
      <li>
        <svg viewBox="0 0 16 16" aria-hidden="true"><path d="M4 1h6l2 2v3h2v9H2V6h2zm1 1v4h6V3.5L9.5 2zM4 9v1.5h2V9zm3 0v1.5h2V9zm3 0v1.5h2V9zM4 11.5V13h2v-1.5zm3 0V13h2v-1.5zm3 0V13h2v-1.5z"/></svg>
        555-203-4471
      </li>
      <li>
        <svg viewBox="0 0 16 16" aria-hidden="true"><path d="M1 3h14v10H1zm1.6 1.2L8 8.4l5.4-4.2z"/></svg>
        mona@tavrelfitness-example.com
      </li>
      <li>
        <svg viewBox="0 0 16 16" aria-hidden="true"><path d="M8 1a7 7 0 1 0 0 14A7 7 0 0 0 8 1zm0 1.2c.9.8 1.6 2.2 1.8 3.8H6.2C6.4 4.4 7.1 3 8 2.2zM2.3 7.2h2.7a11 11 0 0 0 0 1.6H2.3a5.8 5.8 0 0 1 0-1.6zm3.9 0h3.6a10 10 0 0 1 0 1.6H6.2a10 10 0 0 1 0-1.6zm4.8 0h2.7a5.8 5.8 0 0 1 0 1.6H11a11 11 0 0 0 0-1.6zM6.2 10h3.6c-.2 1.6-.9 3-1.8 3.8-.9-.8-1.6-2.2-1.8-3.8z"/></svg>
        www.tavrelfitness-example.com
      </li>
    </ul>
    <div class="front__brand">
      <span class="wordmark">Tavrel</span>
      <span class="wordmark">Fitness</span>
    </div>
  </div>

  <p class="address">214.9th floor.Arcade<br>Kestrel Road VTN</p>

  <div class="holder">
    <p class="holder__name">Mona Lykkestad</p>
    <p class="holder__role">Owner</p>
  </div>
</section>

</body>
</html>
```